Modern Design Business Card industrial maintenance company

Business card design for Company named Brookvale Equipment Services

Target Market(s)

Industrial

Industry/Entity Type

Maintenance and repair

Contact Information for Business Card

Place holder for address, office phone, mobile number and email

Requirements
Must have
• Clean modern look
Nice to have
• N/a

```html
<!DOCTYPE html>
<html lang="en">
<head>
<meta charset="utf-8">
<title>Brookvale Equipment Services – Business Card</title>
<link href="https://fonts.googleapis.com/css2?family=Montserrat:wght@400;600;700&display=swap" rel="stylesheet">
<style>
  :root {
    --backdrop: #d9d8d6;
    --card-light: #ffffff;
    --card-dark: #1c1c1c;
    --ink: #2a2a2a;
    --ink-soft: #3a3a3a;
    --paper-white: #ffffff;
  }
  * { box-sizing: border-box; margin: 0; padding: 0; }
  html, body {
    width: 1200px; height: 1200px; overflow: hidden;
    background: var(--backdrop);
    font-family: "Montserrat", Arial, sans-serif;
  }
  .canvas {
    position: relative; width: 1200px; height: 1200px;
    display: flex; flex-direction: column; align-items: center; justify-content: center; gap: 70px;
  }
  .card {
    width: 700px; height: 400px; border-radius: 4px;
    box-shadow: 0 2px 6px rgba(0,0,0,0.12);
    position: relative;
  }
  .card--front { background: var(--card-light); color: var(--ink); padding: 64px 60px; }
  .card--back { background: var(--card-dark); color: var(--paper-white);
    display: flex; align-items: center; justify-content: center; }

  .brand { display: flex; align-items: center; gap: 18px; }
  .brand__mark { width: 66px; height: 66px; border: 3px solid var(--ink); border-radius: 50%; flex: none; }
  .brand__name { font-weight: 600; line-height: 1; }
  .brand__primary { display: block; font-size: 34px; letter-spacing: 2px; }
  .brand__secondary { display: block; font-size: 11.5px; letter-spacing: 5.2px; margin-top: 6px; }

  .person { margin-top: 70px; }
  .person__name { font-size: 27px; letter-spacing: 0.5px; font-weight: 400; }
  .person__name strong { font-weight: 700; }
  .person__title { font-size: 15px; margin-top: 2px; color: var(--ink-soft); }

  .contact { margin-top: 36px; font-size: 15.5px; line-height: 1.45; color: var(--ink-soft); }

  .back-brand { display: flex; flex-direction: column; align-items: center; gap: 18px; }
  .back-brand__mark { width: 120px; height: 120px; border: 4px solid var(--paper-white); border-radius: 50%; }
  .back-brand__name { font-weight: 600; font-size: 18px; letter-spacing: 4px; text-transform: uppercase; }
</style>
</head>
<body>
<main class="canvas">
  <section class="card card--front" aria-label="Business card front">
    <div class="brand">
      <span class="brand__mark" aria-hidden="true"></span>
      <p class="brand__name">
        <span class="brand__primary">BROOKVALE</span>
        <span class="brand__secondary">EQUIPMENT SERVICES</span>
      </p>
    </div>
    <div class="person">
      <h1 class="person__name"><strong>MARCUS</strong> HALE</h1>
      <p class="person__title">CEO &amp; Founder</p>
    </div>
    <address class="contact" style="font-style:normal">
      48 Harbor Road, Millbrook, Your City<br>
      Email: info@brookvale-mail.com | www.brookvaleservices.com<br>
      Phone: 555-210-7788 | Fax: 555-210-7788
    </address>
  </section>

  <section class="card card--back" aria-label="Business card back">
    <div class="back-brand">
      <span class="back-brand__mark" aria-hidden="true"></span>
      <p class="back-brand__name">Brookvale</p>
    </div>
  </section>
</main>
</body>
</html>
```